Email Design Creative Design Needed

Our website is called CampusLedger.org. One of our competitor(varsity scout.us.com) is using the following email creative.
http://qtr.brightvelmo.com/Affiliate/Assets/3532.html
http://qtr.brightvelmo.com/Affiliate/Assets/7921.html
http://qtr.brightvelmo.com/Affiliate/Assets/8061.html

We would like to use similar email creative without copying their exact creative. You can use the above as a guide but then come up with your own version of the creative.
The above are just concepts, please be creative and come up with your own version of it, without feeling that they have been copied. Feel free to move the components around. Also, feel free to change the colours and text.

Please find attached the CampusLedger.org logo.

Reason: We would like to receive more designs.

Industry/Entity Type

College

```html
<!DOCTYPE html>
<html lang="en">
<head>
<meta charset="utf-8">
<title>Psychology Degrees – Substance Abuse Focus</title>
<link href="https://fonts.googleapis.com/css2?family=Source+Sans+3:wght@400;600;700&display=swap" rel="stylesheet">
<style>
  :root {
    --navy: #15223f;
    --navy-soft: #22355e;
    --amber: #f2a93b;
    --amber-deep: #d98a1c;
    --sky: #dfe8f4;
    --sky-alt: #eef3f9;
    --rule: #c5d2e4;
    --ink: #1d2433;
    --link: #1f4fa8;
    --white: #ffffff;
  }
  * { margin: 0; padding: 0; box-sizing: border-box; }
  html, body { width: 1041px; height: 1200px; overflow: hidden; background: var(--white); }
  .email {
    position: relative; width: 1041px; height: 1200px; overflow: hidden;
    font-family: "Source Sans 3", Arial, sans-serif; color: var(--ink);
  }

  /* Masthead */
  .masthead {
    position: absolute; left: 0; top: 0; width: 1041px; height: 140px;
    background: var(--navy); border-bottom: 6px solid var(--amber);
  }
  .brand {
    position: absolute; left: 48px; top: 22px;
    font-weight: 600; font-size: 22px; line-height: 1; color: var(--white);
    letter-spacing: 0.5px;
  }
  .masthead__title {
    position: absolute; left: 48px; top: 52px;
    font-weight: 700; font-size: 46px; line-height: 1; color: var(--white);
  }
  .masthead__subtitle {
    position: absolute; left: 48px; top: 102px;
    font-weight: 400; font-size: 24px; line-height: 1; color: var(--amber);
  }
  .masthead__tag {
    position: absolute; right: 48px; top: 58px; width: 300px;
    font-weight: 400; font-size: 20px; line-height: 26px; color: var(--sky);
    text-align: right;
  }

  /* Hero image area */
  .hero {
    position: absolute; left: 0; top: 140px; width: 1041px; height: 460px;
    background: linear-gradient(100deg, #2b2b2b 0%, #8a8a8a 40%, #d4d4d4 75%, #bdbdbd 100%);
  }

  /* Call to action */
  .cta {
    position: absolute; left: 0; top: 600px; width: 1041px; height: 130px;
    background: var(--navy-soft);
  }
  .cta__lead {
    position: absolute; left: 48px; top: 28px; width: 560px;
    color: var(--white); font-size: 29px; line-height: 37px; font-weight: 400;
  }
  .cta__button {
    position: absolute; right: 48px; top: 30px; width: 360px; height: 70px;
    background: var(--amber); border-radius: 35px;
    display: flex; align-items: center; justify-content: center; gap: 14px;
    color: var(--navy); font-size: 23px; font-weight: 700; text-decoration: none;
  }
  .cta__button svg { flex: none; }

  /* Career table */
  .careers {
    position: absolute; left: 0; top: 730px; width: 1041px; height: 470px;
    display: grid; grid-template-columns: 400px 260px 381px;
    grid-template-rows: 58px repeat(4, 103px);
  }
  .careers__head {
    background: var(--amber-deep); color: var(--white);
    font-size: 24px; font-weight: 700; display: flex; align-items: center;
    padding-left: 48px;
  }
  .careers__head--salary { justify-content: center; padding-left: 0; }
  .careers__head--steps { padding-left: 24px; }
  .careers__cell {
    display: flex; align-items: center; font-size: 21px; line-height: 28px;
    border-bottom: 1px solid var(--rule); background: var(--sky-alt);
  }
  .careers__cell--even { background: var(--sky); }
  .careers__cell--type { padding-left: 48px; padding-right: 16px; font-weight: 600; }
  .careers__cell--salary { justify-content: center; font-weight: 700; color: var(--navy-soft); }
  .careers__cell--steps { padding-left: 24px; padding-right: 24px; }
  .careers a { color: var(--link); text-decoration: underline; }
</style>
</head>
<body>
<div class="email">
  <header class="masthead">
    <span class="brand">CampusLedger</span>
    <h1 class="masthead__title">Psychology Degrees</h1>
    <p class="masthead__subtitle">With a Concentration in Substance Abuse</p>
    <p class="masthead__tag">Turn your interest in the mind into a career that helps people recover.</p>
  </header>

  <div class="hero" role="img" aria-label="Black and white photo of a young person looking down, softly lit from the right"></div>

  <section class="cta">
    <p class="cta__lead">Find psychology programs focused on<br>substance abuse and recovery.</p>
    <a class="cta__button" href="#">
      Get Program &amp; Aid Info
      <svg width="26" height="26" viewBox="0 0 26 26" aria-hidden="true">
        <circle cx="13" cy="13" r="13" fill="var(--navy)"/>
        <path d="M9 7 L16 13 L9 19" fill="none" stroke="var(--amber)" stroke-width="3" stroke-linecap="round" stroke-linejoin="round"/>
      </svg>
    </a>
  </section>

  <div class="careers">
    <div class="careers__head">Career Path</div>
    <div class="careers__head careers__head--salary">Median Salary</div>
    <div class="careers__head careers__head--steps">Next Steps</div>

    <div class="careers__cell careers__cell--type">Substance Abuse and Behavioral Disorder Counselors</div>
    <div class="careers__cell careers__cell--salary">$41,030 per year*</div>
    <div class="careers__cell careers__cell--steps"><a href="#">Browse Behavioral Disorder Counseling Programs</a></div>

    <div class="careers__cell careers__cell--even careers__cell--type">Mental Health and Substance Abuse Social Workers</div>
    <div class="careers__cell careers__cell--even careers__cell--salary">$42,650 per year*</div>
    <div class="careers__cell careers__cell--even careers__cell--steps"><a href="#">Browse Social Work Programs</a></div>

    <div class="careers__cell careers__cell--type">Rehabilitation Counselors</div>
    <div class="careers__cell careers__cell--salary">$37,070 per year*</div>
    <div class="careers__cell careers__cell--steps"><a href="#">Browse Rehabilitation Counseling Programs</a></div>

    <div class="careers__cell careers__cell--even careers__cell--type">Mental Health Counselors</div>
    <div class="careers__cell careers__cell--even careers__cell--salary">$42,590 per year*</div>
    <div class="careers__cell careers__cell--even careers__cell--steps"><a href="#">Browse Mental Health Counseling Programs</a></div>
  </div>
</div>
</body>
</html>
```